Dorvelan Swimming & Athletics Center

We need Business Card for a Athletics center
The logo frome the Uploaded Files ( b card fimal)
Οn one side of card we need the logo of company the Contact and the website:
1. Address:(Limassol, Cyprus 12-14 Stavrinelou str,Ano Trimeni,P.C. 4832)

2.Phone number: (+357) 25-704263

3. Mail: info@dorvelanfit.example

3. Website: www.dorvelanfit.example

Οn the other side of the card we need to write the sport of the company:

1. Artistic Gymnastics
2. Swimming
3. Gym - Fitness
4. Programs
5. Dancing
5.Tennis

From the Uploaded Files you can get the logo.In a logo is behind the black color which can be removed from logo.

Υou can use that color you want.
.
Updates

Industry/Entity Type

Business

Font styles to use
Decorative

Colors
0555a3
ffcf3e
3176b5
0692cd
add136
f04a50
000000
cfcfcf
9d9d9d

Requirements
Should not have
• photos with faces
• photo fro the Website:www.dorvelanfit.example

```html
<!DOCTYPE html>
<html lang="en">
<head>
<meta charset="utf-8">
<title>Dorvelan Business Card</title>
<link rel="stylesheet" href="https://fonts.googleapis.com/css2?family=Montserrat:wght@500;600;800&display=swap">
<style>
  :root {
    --backdrop: #1b1b1d;
    --card: #26272b;
    --gold: #f6ac1e;
    --icon: #f0a21a;
    --white: #f4f4f4;
    --ring: rgba(255,255,255,0.05);
  }
  * { margin: 0; padding: 0; box-sizing: border-box; }
  html, body {
    width: 1189px; height: 1200px; overflow: hidden;
    background: var(--backdrop);
    font-family: "Montserrat", sans-serif;
    color: var(--white);
  }
  .card {
    position: absolute; left: 172px; width: 854px; height: 487px;
    background: var(--card);
    box-shadow: 0 6px 18px rgba(0,0,0,0.55);
    overflow: hidden;
  }
  .card--front { top: 68px; }
  .card--back { top: 627px; }

  .backdrop-ring {
    position: absolute; left: 178px; top: 0; width: 498px; height: 498px;
    border: 14px solid var(--ring); border-radius: 50%;
  }
  .brand-name {
    position: absolute; font-weight: 800; color: var(--gold);
    letter-spacing: 1px; line-height: 1; white-space: nowrap;
  }
  .card--front .brand-name { left: 0; width: 100%; text-align: center; top: 104px; font-size: 84px; }
  .center-title {
    position: absolute; left: 0; width: 100%; top: 231px; text-align: center;
    font-weight: 500; font-size: 27px; line-height: 39px; letter-spacing: 0.3px;
  }
  .sports-list {
    position: absolute; left: 0; width: 100%; top: 348px; text-align: center;
    font-weight: 500; font-size: 21px; line-height: 29px;
  }

  .card--back .brand-name { left: 48px; top: 94px; font-size: 80px; }
  .brand-mark {
    position: absolute; left: 560px; top: 68px; width: 108px; height: 108px;
    border: 3px solid var(--gold); border-radius: 50%;
  }
  .holder {
    position: absolute; right: 47px; top: 256px; text-align: right; line-height: 1;
  }
  .holder-name { font-weight: 800; font-size: 30px; color: var(--gold); letter-spacing: 0.5px; }
  .holder-role { font-weight: 500; font-size: 21px; margin-top: 2px; }
  .divider {
    position: absolute; left: 50px; top: 295px; width: 650px; height: 2px; background: var(--white);
  }
  .contact-list {
    position: absolute; left: 50px; top: 366px; list-style: none;
    font-weight: 500; font-size: 21px; line-height: 30px;
  }
  .contact-list li { display: flex; align-items: center; gap: 10px; }
  .contact-icon { width: 24px; height: 24px; flex: none; }
  .address {
    position: absolute; right: 47px; top: 366px; text-align: right;
    font-weight: 500; font-size: 21px; line-height: 29px;
  }
</style>
</head>
<body>
  <section class="card card--front">
    <div class="backdrop-ring"></div>
    <div class="brand-name">DORVELAN</div>
    <h1 class="center-title">DORVELAN SWIMMING<br>&amp; ATHLETICS CENTER</h1>
    <p class="sports-list">ARTISTIC GYMNASTICS | SWIMMING<br>GYM - FITNESS | PROGRAMS | DANCING | TENNIS</p>
  </section>

  <section class="card card--back">
    <div class="brand-name">DORVELAN</div>
    <div class="brand-mark"></div>
    <div class="holder">
      <div class="holder-name">MARIN ALDOUS</div>
      <div class="holder-role">Owner</div>
    </div>
    <div class="divider"></div>
    <ul class="contact-list">
      <li>
        <svg class="contact-icon" viewBox="0 0 24 24"><rect width="24" height="24" rx="2" fill="var(--icon)"/><path d="M5 10c0-3 14-3 14 0v2h-4v-2H9v2H5z M7 13h10l1 6H6z" fill="#2a2118"/></svg>
        (+357) 25-704263
      </li>
      <li>
        <svg class="contact-icon" viewBox="0 0 24 24"><rect width="24" height="24" rx="2" fill="var(--icon)"/><rect x="5" y="7" width="14" height="10" fill="none" stroke="#2a2118" stroke-width="1.6"/><path d="M5 7l7 6 7-6" fill="none" stroke="#2a2118" stroke-width="1.6"/></svg>
        info@dorvelanfit.example
      </li>
      <li>
        <svg class="contact-icon" viewBox="0 0 24 24"><rect width="24" height="24" rx="2" fill="var(--icon)"/><g fill="none" stroke="#2a2118" stroke-width="1.4"><circle cx="12" cy="12" r="7"/><ellipse cx="12" cy="12" rx="3" ry="7"/><path d="M5 12h14M6 8.5h12M6 15.5h12"/></g></svg>
        www.dorvelanfit.example
      </li>
    </ul>
    <p class="address">Limassol,<br>Cyprus 12-14 Stavrinelou str,<br>Ano Trimeni,P.C. 4832</p>
  </section>
</body>
</html>
```